Urine collection cup with and without sterile seal sticker

Hello. We need a urine cup label designed please with

Name:
Date of Birth:
Date:
Time:
Temp℃:
Specimen ID:

Product code: TUB-47
Volume markings (e.g., 30 mL, 60 mL, 90 mL).
Vela Drug Tests logo

Could you please provide one version with the additional sterile sticker extending to the top, and one version without the additional sterile sticker?

```html
<!DOCTYPE html>
<html lang="en">
<head>
<meta charset="utf-8">
<title>Vela Drug Tests – Urine Cup Labels</title>
<link rel="stylesheet" href="https://fonts.googleapis.com/css2?family=Montserrat:wght@400;500;700&display=swap">
<style>
  :root {
    --navy: #2e2883;
    --rule: #7d72c2;
    --code-blue: #2f9bd7;
    --teal: #36b9c6;
    --white: #ffffff;
    --page: #ffffff;
  }
  * { box-sizing: border-box; margin: 0; padding: 0; }
  html, body {
    width: 1200px; height: 1200px; overflow: hidden;
    background: var(--page);
    font-family: "Montserrat", Arial, sans-serif;
  }
  .sheet { position: relative; width: 1200px; height: 1200px; }

  .cup-label { position: absolute; left: 171px; height: 508px; }
  .cup-label--sealed { top: 71px; width: 938px; }
  .cup-label--plain { top: 628px; width: 552px; }
  .cup-label__shape { position: absolute; inset: 0; }

  .seal-text {
    position: absolute; left: 690px; top: 22px; width: 212px;
    text-align: center; line-height: 1;
  }
  .seal-text__title {
    display: block; color: var(--teal);
    font-weight: 700; font-size: 33px; letter-spacing: 0.3px;
  }
  .seal-text__sub {
    display: block; margin-top: 4px; color: var(--white);
    font-weight: 400; font-size: 22px; white-space: nowrap;
  }

  .record-panel {
    position: absolute; left: 27px; top: 29px; width: 499px; height: 384px;
    background: var(--white); border-radius: 25px;
  }
  .field {
    position: absolute; left: 21px; right: 31px; top: var(--row);
    display: flex; align-items: baseline;
    color: var(--navy); font-size: 22px; line-height: 1; font-weight: 400;
  }
  .field__name { white-space: nowrap; padding-right: 5px; }
  .field__line { flex: 1; border-bottom: 1px solid var(--rule); transform: translateY(-3px); }
  .product-code {
    position: absolute; left: 0; right: 0; top: 349px;
    text-align: center; color: var(--code-blue);
    font-weight: 700; font-size: 25px; line-height: 1;
  }

  .brand-name {
    position: absolute; left: 0; width: 552px; top: 440px; height: 56px;
    display: flex; align-items: center; justify-content: center;
    color: var(--white); font-weight: 700; font-size: 26px;
    letter-spacing: 0.5px; white-space: nowrap;
  }
</style>
</head>
<body>
<main class="sheet">

  <section class="cup-label cup-label--sealed" aria-label="Cup label with sterile seal tab">
    <svg class="cup-label__shape" width="938" height="508" viewBox="0 0 938 508" aria-hidden="true">
      <path fill="var(--navy)" d="M41,0 H896 A42,42 0 0 1 938,42 V63 A42,42 0 0 1 896,105 H552 V467 A41,41 0 0 1 511,508 H41 A41,41 0 0 1 0,467 V41 A41,41 0 0 1 41,0 Z"/>
    </svg>
    <p class="seal-text">
      <span class="seal-text__title">STERILE</span>
      <span class="seal-text__sub">READY FOR USE</span>
    </p>
    <div class="record-panel">
      <p class="field" style="--row:40px"><span class="field__name">NAME:</span><span class="field__line"></span></p>
      <p class="field" style="--row:86px"><span class="field__name">DATE OF BIRTH:</span><span class="field__line"></span></p>
      <p class="field" style="--row:129px"><span class="field__name">DATE:</span><span class="field__line"></span></p>
      <p class="field" style="--row:176px"><span class="field__name">TIME:</span><span class="field__line"></span></p>
      <p class="field" style="--row:225px"><span class="field__name">TEMP℃:</span><span class="field__line"></span></p>
      <p class="field" style="--row:275px"><span class="field__name">SPECIMEN ID:</span><span class="field__line"></span></p>
      <p class="product-code">Product code: TUB-47</p>
    </div>
    <p class="brand-name">VELA DRUG TESTS</p>
  </section>

  <section class="cup-label cup-label--plain" aria-label="Cup label without sterile seal">
    <svg class="cup-label__shape" width="552" height="508" viewBox="0 0 552 508" aria-hidden="true">
      <rect width="552" height="508" rx="41" fill="var(--navy)"/>
    </svg>
    <div class="record-panel">
      <p class="field" style="--row:40px"><span class="field__name">NAME:</span><span class="field__line"></span></p>
      <p class="field" style="--row:86px"><span class="field__name">DATE OF BIRTH:</span><span class="field__line"></span></p>
      <p class="field" style="--row:129px"><span class="field__name">DATE:</span><span class="field__line"></span></p>
      <p class="field" style="--row:176px"><span class="field__name">TIME:</span><span class="field__line"></span></p>
      <p class="field" style="--row:225px"><span class="field__name">TEMP℃:</span><span class="field__line"></span></p>
      <p class="field" style="--row:275px"><span class="field__name">SPECIMEN ID:</span><span class="field__line"></span></p>
      <p class="product-code">Product code: TUB-47</p>
    </div>
    <p class="brand-name">VELA DRUG TESTS</p>
  </section>

</main>
</body>
</html>
```